Wellmere Talking Therapies House

We need a design for magazine advert, ideally high resolution to advertise our counselling centre. we would like this to include a photo of two people talking, as if in a counselling session. See our logo and colour range on our website. www.wellmere-house.co.uk
The photo should not include cups of coffee, clipboards, desks, people touching. it needs to be two people in armchairs sympathetically listening and looking at each other.
The font type is Great Vibes on the logo. Our design should communicate a centre of excellence delivering high quality, professional services in stylishly furnished surroundings.
Updates

Hello Everyone We have had a number of designs that look quite promising but are missing the brief. Can I reiterate that we need a photograph of 2 people seated talking to each other in a sincere way. There shouldn't be office chairs but comfortable chairs. There should be no physical contact. There should be no clipboards.Thank you very muchHeather Added Sunday, March 12, 2017

Target Market(s)

people seeking counselling and psychotherapy

Font styles to use
Other font styles liked:
• Great Vibes as in our logo for some of the print. See attached file.

Requirements
Must have
• good photograph
• Two high res Pixelvane photos:
• https://pixelvane-files.example-portal.net/download/photo-one-ref-7341
• https://pixelvane-files.example-portal.net/download/photo-two-ref-9826
Nice to have
• Watermark in keeping with our logo.
Should not have
• Darkness

```html
<!DOCTYPE html>
<html lang="en">
<head>
<meta charset="utf-8">
<title>Wellmere Talking Therapies House – Advert</title>
<link rel="stylesheet" href="https://fonts.googleapis.com/css2?family=Lato:ital,wght@0,400;0,700;1,400&family=Oswald:wght@400;500;700&family=Playball&display=swap">
<style>
  :root {
    --backdrop: #ecebe7;
    --paper: #ffffff;
    --ink: #3a3333;
    --ink-soft: #555050;
    --olive: #98984a;
    --olive-line: #8a8f1e;
    --sage: #7c9e78;
    --photo-light: #eef0f1;
    --photo-mid: #c9cfd3;
  }
  * { margin: 0; padding: 0; box-sizing: border-box; }
  html, body { width: 1200px; height: 1200px; overflow: hidden; background: var(--backdrop); }
  .advert {
    position: absolute; left: 200px; top: 35px;
    width: 800px; height: 1130px;
    background: var(--paper); overflow: hidden;
    box-shadow: 0 4px 16px rgba(0,0,0,0.15);
    font-family: 'Lato', sans-serif; color: var(--ink);
  }
  .header-art { position: absolute; left: 0; top: 0; width: 800px; height: 500px; }
  .brand {
    position: absolute; left: 40px; top: 70px; width: 260px;
    display: flex; flex-direction: column; align-items: center; gap: 12px;
  }
  .brand-dot { width: 36px; height: 36px; border-radius: 50%; background: var(--olive); }
  .brand-name {
    font-family: 'Lato', sans-serif; font-weight: 700; font-size: 19px;
    color: var(--ink); text-align: center; line-height: 1.25; letter-spacing: 0.5px;
  }
  .quote {
    position: absolute; left: 50px; top: 514px; width: 700px;
    font-style: italic; font-size: 22.5px; line-height: 31px; color: var(--ink-soft);
    text-align: center; white-space: nowrap;
  }
  .quote-mark {
    font-family: 'Oswald', sans-serif; font-style: normal; font-weight: 700;
    font-size: 40px; color: var(--sage); vertical-align: -12px; line-height: 0;
  }
  .quote-author {
    position: absolute; right: 75px; top: 584px;
    font-size: 22.5px; line-height: 28px; color: var(--ink-soft);
  }
  .headline {
    position: absolute; left: 0; top: 644px; width: 800px;
    font-family: 'Playball', cursive; font-weight: 400; font-size: 56px; line-height: 56px;
    text-align: center; color: var(--ink);
  }
  .headline .small { font-size: 46px; }
  .intro {
    position: absolute; left: 57px; top: 840px; width: 685px;
    font-size: 23px; line-height: 31.5px; color: var(--ink);
  }
  .intro .line { display: block; text-align: justify; text-align-last: justify; }
  .intro .line-last { display: block; text-align: center; }
  .footer-art { position: absolute; left: 0; top: 900px; width: 800px; height: 230px; }
  .appointments {
    position: absolute; left: 69px; top: 1000px; width: 300px;
    font-family: 'Oswald', sans-serif; color: #fff; line-height: 1;
  }
  .appointments .label { font-size: 33px; font-weight: 500; letter-spacing: 1px; }
  .appointments .big { font-size: 48px; font-weight: 500; margin-top: 4px; letter-spacing: 0.5px; }
  .appointments .note { font-size: 17px; font-weight: 400; margin-top: 6px; }
  .contact {
    position: absolute; left: 545px; top: 1040px; list-style: none;
    font-size: 17px; line-height: 20px; color: #fff;
  }
  .contact li { display: flex; align-items: flex-start; gap: 6px; margin-bottom: 1px; }
  .contact svg { flex: none; margin-top: 3px; }
</style>
</head>
<body>
  <main class="advert">
    <svg class="header-art" viewBox="0 0 800 500">
      <defs>
        <clipPath id="photo-shape">
          <polygon points="0,0 800,0 800,289 241,495 0,394"/>
        </clipPath>
        <linearGradient id="photo-tone" x1="0" y1="0" x2="1" y2="1">
          <stop offset="0" stop-color="#ffffff"/>
          <stop offset="0.45" stop-color="#eef0f1"/>
          <stop offset="1" stop-color="#c9cfd3"/>
        </linearGradient>
      </defs>
      <rect role="img" aria-label="Photograph of an older woman and a therapist seated, smiling and talking in a bright consulting room" width="800" height="500" fill="url(#photo-tone)" clip-path="url(#photo-shape)"/>
      <polyline points="0,394 241,495 800,289" fill="none" stroke="var(--olive-line)" stroke-width="3"/>
    </svg>

    <div class="brand">
      <span class="brand-dot"></span>
      <span class="brand-name">Wellmere Talking<br>Therapies House</span>
    </div>

    <p class="quote"><span class="quote-mark">&ldquo;</span>A big port of letting go is recognising when it is time to stay in a<br>situation and when it is time to move on. <span class="quote-mark">&rdquo;</span></p>
    <p class="quote-author">Marian E. Holloway</p>

    <h1 class="headline">Confidential Therapeutic Services<br><span class="small">in the</span><br>Heart of Old Town</h1>

    <p class="intro">
      <span class="line">We have over 30 carefully selected, qualified and professional</span>
      <span class="line">therapists offering a range of services to help individuals,</span>
      <span class="line-last">families and couples.</span>
    </p>

    <svg class="footer-art" viewBox="0 0 800 230" aria-hidden="true">
      <polygon points="330,230 800,5 800,230" fill="var(--sage)"/>
      <circle cx="184" cy="277" r="254" fill="var(--olive)"/>
      <circle cx="184" cy="277" r="244" fill="none" stroke="#fff" stroke-width="2"/>
    </svg>

    <div class="appointments">
      <div class="label">APPOINTMENTS</div>
      <div class="big">AVAILABLE</div>
      <div class="note">throughout the clay and evening</div>
    </div>

    <ul class="contact">
      <li>
        <svg width="14" height="16" viewBox="0 0 14 16"><path d="M7 1a5 5 0 0 0-5 5c0 4 5 9 5 9s5-5 5-9a5 5 0 0 0-5-5z" fill="none" stroke="#fff" stroke-width="1.6"/><circle cx="7" cy="6" r="1.8" fill="#fff"/></svg>
        <span>14 Linden Row, Old Town,<br>Ashcombe AC2 7LR</span>
      </li>
      <li>
        <svg width="16" height="14" viewBox="0 0 16 14"><rect x="1" y="2" width="14" height="10" rx="1.5" fill="none" stroke="#fff" stroke-width="1.5"/><rect x="3.5" y="4" width="3" height="6" fill="#fff"/><path d="M9 5h4M9 7h4M9 9h4" stroke="#fff" stroke-width="1"/></svg>
        <span>01632 960418</span>
      </li>
      <li>
        <svg width="16" height="14" viewBox="0 0 16 14"><path d="M1 10l7-6 3 3 4-5M1 13h14" fill="none" stroke="#fff" stroke-width="1.7" stroke-linecap="round"/></svg>
        <span>www.wellmere-house.co.uk</span>
      </li>
    </ul>
  </main>
</body>
</html>
```